Business Cards for a law firm

Business cards for our law firm. Use our silhoette logo and OAK HARBOR - check our website (www.oakharbor-legal.com)

Contact Information for Business Card

our silhouette logo, OAK HARBOR, 800-555-0147, Dorian Kestrup, dorian@oakharbor-legal.com

Requirements
Must have
• our silhouette logo, OAK HARBOR, 800-555-0147, Dorian Kestrup, dorian@oakharbor-legal.com

```html
<!DOCTYPE html>
<html lang="en">
<head>
<meta charset="utf-8">
<title>Oak Harbor – Business Cards</title>
<link href="https://fonts.googleapis.com/css2?family=Michroma&family=Lato:wght@400;700&family=Libre+Baskerville&display=swap" rel="stylesheet">
<style>
  :root {
    --stage: #2b2f36;
    --navy: #3a4e72;
    --navy-deep: #2c3d5c;
    --ink: #1c2536;
    --gold: #f9b733;
    --white: #ffffff;
    --silver: #c9ced8;
    --suit-dark: #1f2433;
    --suit-light: #6b6f7d;
  }
  * { margin: 0; padding: 0; box-sizing: border-box; }
  html, body {
    width: 1200px; height: 985px; overflow: hidden;
    background: var(--stage);
  }
  .canvas { position: relative; width: 1200px; height: 985px; }
  .card {
    position: absolute;
    width: 540px; height: 309px;
    border-radius: 22px;
    overflow: hidden;
    box-shadow: 0 14px 30px rgba(0,0,0,.45);
  }
  .card--front { left: 40px; top: 338px; background: var(--white); }
  .card--back  { left: 620px; top: 338px; background: var(--navy); }

  .card__art { position: absolute; inset: 0; width: 100%; height: 100%; }

  .brand {
    position: absolute;
    display: flex; align-items: center; gap: 14px;
  }
  .brand__mark { flex: none; display: block; }
  .card--front .brand { left: 250px; top: 70px; }
  .card--front .brand__mark { width: 50px; height: 50px; background: var(--white); }
  .card--back .brand { left: 110px; top: 100px; }
  .card--back .brand__mark { width: 58px; height: 58px; background: var(--ink); }

  .wordmark {
    font-family: "Michroma", sans-serif;
    color: var(--white);
    line-height: 1;
  }
  .wordmark__top { font-size: 20px; letter-spacing: 2px; }
  .wordmark__main { font-size: 30px; letter-spacing: 2px; margin-top: 6px; }
  .card--back .wordmark { color: var(--silver); }
  .card--back .wordmark__top { font-size: 22px; }
  .card--back .wordmark__main { font-size: 32px; }

  .name-tag {
    position: absolute; left: 240px; top: 154px;
    font-family: "Lato", sans-serif; font-size: 19px;
    letter-spacing: 1px; color: var(--navy-deep);
  }

  .contacts {
    position: absolute; left: 250px; top: 204px;
    font-family: "Libre Baskerville", serif; font-size: 13px;
    color: var(--white); list-style: none;
  }
  .contacts li { display: flex; align-items: center; gap: 8px; height: 22px; }
  .contacts svg { width: 14px; height: 14px; flex: none; }

  .website { position: absolute; font-family: "Libre Baskerville", serif; }
  .card--front .website {
    left: 230px; top: 258px; font-size: 15px;
    letter-spacing: 3px; color: var(--gold);
  }
  .card--back .website {
    left: 120px; top: 200px; font-size: 11px;
    letter-spacing: 6px; color: var(--white);
  }
</style>
</head>
<body>
<main class="canvas">

  <section class="card card--front" aria-label="Business card front">
    <svg class="card__art" viewBox="0 0 540 309">
      <defs>
        <linearGradient id="portrait-tones" x1="0" y1="0" x2="1" y2="1">
          <stop offset="0" stop-color="#6b6f7d"/>
          <stop offset="1" stop-color="#1f2433"/>
        </linearGradient>
      </defs>
      <rect class="portrait" x="0" y="40" width="215" height="269" fill="url(#portrait-tones)" role="img" aria-label="Portrait photo of the attorney in a dark suit"/>
      <polygon class="accent-wedge" points="330,0 540,0 540,72 330,49" fill="#f9b733"/>
      <polygon class="panel" points="175,309 175,110 235,40 540,72 540,309" fill="#3a4e72"/>
      <rect class="base-band" x="175" y="290" width="365" height="19" fill="#f9b733"/>
      <polygon class="name-band" points="215,165 235,145 540,145 540,185 235,185" fill="#f9b733"/>
    </svg>

    <div class="brand">
      <span class="brand__mark" role="img" aria-label="Firm logo mark"></span>
      <div class="wordmark">
        <div class="wordmark__top">OAK</div>
        <div class="wordmark__main">HARBOR</div>
      </div>
    </div>

    <div class="name-tag">DORIAN KESTRUP</div>

    <ul class="contacts">
      <li>
        <svg viewBox="0 0 14 14"><circle cx="7" cy="7" r="7" fill="#f9b733"/><path d="M4.5 3.5l1.6 1.6-.9 1a5 5 0 0 0 2.7 2.7l1-.9 1.6 1.6-1 1.1c-2.8-.3-5.3-2.8-5.6-5.6z" fill="#2c3d5c"/></svg>
        800-555-0147
      </li>
      <li>
        <svg viewBox="0 0 14 14"><circle cx="7" cy="7" r="7" fill="#f9b733"/><rect x="3.5" y="4.5" width="7" height="5" fill="none" stroke="#2c3d5c" stroke-width="1"/><path d="M3.5 4.5L7 7.5l3.5-3" fill="none" stroke="#2c3d5c" stroke-width="1"/></svg>
        dorian@oakharbor-legal.com
      </li>
    </ul>

    <div class="website">www.oakharbor-legal.com</div>
  </section>

  <section class="card card--back" aria-label="Business card back">
    <div class="brand">
      <span class="brand__mark" role="img" aria-label="Firm logo mark"></span>
      <div class="wordmark">
        <div class="wordmark__top">OAK</div>
        <div class="wordmark__main">HARBOR</div>
      </div>
    </div>
    <div class="website">www.oakharbor-legal.com</div>
  </section>

</main>
</body>
</html>
```